Quelvane FZE
Engineered for Silence
Quelvane FZE -
Creative Brief
Use specific fonts
Use your own creativity
Professional
T. Orlov
Managing Director & Chief Acoustic Consultant
P.O. Box - 58914, Ras Al Khaimah, U.A.E.
info@quelvane-example.com
www.quelvane-example.com
Please provide Business card, letter head, quotation, invoice, fax & envelop designs
Services & Products: Acoustic Consultants, Acoustic Contracting, Acoustic Spray, Acoustic Underlay, Load Bearing Pads, Acoustic Louvers, Sound Attenuators, Inertia Bases, Floating Floors, Acoustic Doors, Acoustic Barriers, Acoustic Enclosure, Generator Enclosure, Sand Trap Louvers, Extract Louvers, MEP Contracting

```html
<!DOCTYPE html>
<html lang="en">
<head>
<meta charset="utf-8">
<title>Quelvane FZE – Stationery Set</title>
<link href="https://fonts.googleapis.com/css2?family=Open+Sans:wght@400;600;700&display=swap" rel="stylesheet">
<style>
:root{
  --navy:#1d3f8f;
  --blue:#2657b8;
  --teal:#1e9a7a;
  --green:#3bb56a;
  --ink:#333a45;
  --line:#9aa3b5;
  --paper:#ffffff;
  --card-dark:#4a4f57;
}
*{box-sizing:border-box;margin:0;padding:0}
html,body{width:1200px;height:386px;overflow:hidden}
body{font-family:"Open Sans",Arial,sans-serif;color:var(--ink)}
.canvas{position:relative;width:1200px;height:386px;
  background:linear-gradient(90deg,#fff 0,#fff 44%,#cfe9dc 52%,var(--green) 62%,var(--teal) 72%,var(--blue) 86%,var(--navy) 100%);}
.label{position:absolute;font-size:6px;color:#555;letter-spacing:.2px;white-space:nowrap}
.label.light{color:#e6eefc}
.sheet{position:absolute;background:var(--paper);box-shadow:0 1px 4px rgba(0,0,0,.25)}
.brand{position:absolute;display:flex;align-items:center;gap:3px;font-weight:700;color:var(--navy);white-space:nowrap}
.brand .dot{border-radius:50%;background:var(--teal);flex:none}
.contact{position:absolute;font-size:4px;line-height:5.5px;color:var(--ink);white-space:nowrap}
/* fax */
.fax{left:36px;top:30px;width:216px;height:330px}
.fax-word{position:absolute;left:10px;top:22px;font-size:20px;font-weight:700;color:var(--navy);writing-mode:vertical-rl;transform:rotate(180deg);letter-spacing:2px}
.form-grid{position:absolute;left:38px;top:80px;width:166px;border:1px solid var(--line)}
.form-grid div{height:11px;border-bottom:1px solid var(--line);font-size:4px;padding:3px 2px}
.fax-body{position:absolute;left:38px;top:150px;width:166px;height:168px;border:1px solid var(--line)}
.checks{position:absolute;left:38px;top:140px;display:flex;gap:12px;font-size:4px}
.checks span::before{content:"";display:inline-block;width:4px;height:4px;border:1px solid var(--line);margin-right:2px;vertical-align:middle}
/* invoice */
.invoice{left:270px;top:30px;width:212px;height:330px}
.inv-title{position:absolute;left:14px;top:70px;font-size:6px;font-weight:700;color:var(--navy)}
.inv-table{position:absolute;left:14px;top:118px;width:184px;border-collapse:collapse;font-size:4px}
.inv-table th{background:var(--navy);color:#fff;padding:2px;text-align:left;font-weight:600}
.inv-table td{border:1px solid var(--line);height:68px}
.totals{position:absolute;left:140px;top:194px;width:58px;font-size:4px}
.totals div{border:1px solid var(--line);border-top:none;height:9px;padding:2px}
.boxrow{position:absolute;left:14px;top:84px;width:184px;height:26px;border:1px solid var(--line)}
/* letterhead */
.letterhead{left:576px;top:28px;width:218px;height:290px}
/* envelope */
.envelope{left:448px;top:128px;width:262px;height:185px}
.env-window{position:absolute;left:40px;top:104px;width:110px;height:36px;border:1px solid var(--line);border-radius:3px}
/* cards */
.card{position:absolute;width:150px;height:86px;background:var(--paper);box-shadow:0 1px 4px rgba(0,0,0,.35);overflow:hidden}
.card-back{background:var(--card-dark);color:#fff}
.card-back h4{position:absolute;left:10px;bottom:10px;font-size:5px;font-weight:700;letter-spacing:.5px}
.card-back p{position:absolute;left:10px;top:12px;width:120px;font-size:3.6px;line-height:5px;color:#dde}
.name{position:absolute;font-size:5px;font-weight:700;color:var(--navy)}
.band{position:absolute;background:var(--teal)}
</style>
</head>
<body>
<main class="canvas">

  <span class="label" style="left:110px;top:18px">Fax Cover letter</span>
  <section class="sheet fax">
    <div class="brand" style="left:100px;top:14px;font-size:10px"><span class="dot" style="width:9px;height:9px"></span>QuelvaneFZE</div>
    <div class="contact" style="left:100px;top:30px">P.O. Box - 58914<br>Ras Al Khaimah, U.A.E.<br>info@quelvane-example.com<br>www.quelvane-example.com</div>
    <div class="fax-word">FAX</div>
    <div class="form-grid">
      <div>To:</div><div>From:</div><div>Pages:</div><div>Date:</div><div>Re:</div>
    </div>
    <div class="checks"><span>Urgent</span><span>Review</span><span>Reply</span><span>Recycle</span></div>
    <div class="fax-body"></div>
  </section>

  <span class="label" style="left:360px;top:18px">Invoice</span>
  <section class="sheet invoice">
    <div class="brand" style="left:112px;top:18px;font-size:10px"><span class="dot" style="width:9px;height:9px"></span>QuelvaneFZE</div>
    <div class="contact" style="left:124px;top:33px">P.O. Box - 58914<br>Ras Al Khaimah, U.A.E.</div>
    <div class="inv-title">INVOICE</div>
    <div class="boxrow"></div>
    <table class="inv-table">
      <tr><th>No.</th><th>Description</th><th>Qty</th><th>Rate</th><th>Amount</th></tr>
      <tr><td></td><td></td><td></td><td></td><td></td></tr>
    </table>
    <div class="totals"><div>Subtotal</div><div>Tax</div><div>Total</div></div>
  </section>

  <span class="label light" style="left:650px;top:16px">Letterhead A4 8.5x11</span>
  <section class="sheet letterhead">
    <div class="brand" style="left:112px;top:16px;font-size:11px"><span class="dot" style="width:9px;height:9px"></span>QuelvaneFZE</div>
    <div class="contact" style="left:124px;top:32px">P.O. Box - 58914<br>Ras Al Khaimah, U.A.E.<br>info@quelvane-example.com</div>
  </section>

  <section class="sheet envelope">
    <svg width="262" height="185" style="position:absolute;left:0;top:0">
      <polyline points="0,0 131,70 262,0" fill="none" stroke="#c8cdd8" stroke-width="1"/>
    </svg>
    <div class="brand" style="left:14px;top:80px;font-size:11px"><span class="dot" style="width:9px;height:9px"></span>QuelvaneFZE</div>
    <div class="env-window"></div>
    <div class="contact" style="left:180px;top:154px">P.O. Box - 58914<br>Ras Al Khaimah, U.A.E.</div>
    <div class="band" style="left:0;bottom:0;width:262px;height:4px"></div>
  </section>
  <span class="label light" style="left:560px;top:318px">Envelope DL size</span>

  <span class="label light" style="left:1000px;top:30px">Business Card</span>
  <article class="card" style="left:830px;top:44px">
    <div class="brand" style="left:8px;top:10px;font-size:9px"><span class="dot" style="width:7px;height:7px"></span>QuelvaneFZE</div>
    <div class="contact" style="left:8px;top:56px">P.O. Box - 58914, Ras Al Khaimah<br>info@quelvane-example.com<br>www.quelvane-example.com</div>
    <div class="band" style="left:0;bottom:0;width:150px;height:3px"></div>
  </article>
  <article class="card" style="left:860px;top:142px">
    <div class="name" style="left:8px;top:10px">T. Orlov</div>
    <div class="contact" style="left:8px;top:18px">Managing Director &amp;<br>Chief Acoustic Consultant</div>
    <div class="brand" style="left:8px;top:44px;font-size:8px"><span class="dot" style="width:6px;height:6px"></span>QuelvaneFZE</div>
    <div class="contact" style="left:8px;top:60px">info@quelvane-example.com<br>www.quelvane-example.com</div>
    <div class="band" style="left:0;bottom:0;width:150px;height:3px"></div>
  </article>
  <article class="card card-back" style="left:880px;top:250px">
    <p>Acoustic Consultants, Acoustic Contracting, Acoustic Spray, Acoustic Underlay, Load Bearing Pads, Acoustic Louvers, Sound Attenuators, Floating Floors, Acoustic Doors</p>
    <h4>SERVICES &amp; PRODUCTS</h4>
  </article>
  <span class="label light" style="left:1050px;top:340px">Reverse Side</span>

</main>
</body>
</html>
```